Need design for an App.

The app in question is related to security and crime events with real time feed, engagement with friends and posting pictures, we want a sleak, minimal style. There are 11 or 12 screens to be made. We are adding video file as suggestion. We are not sure about colors so we accept suggestions. We are also adding the logo.

Reason: Just giving more time to designers. Thanks.

Industry/Entity Type

Security

Font styles to use
Sans Serif

Requirements
Must have
• The app must have a Login view; a new user view (with nickname, email and pass); a retrieve pass view; a menu view with options for alert configuration, send emergency alert and send report, a feed view with the most popular reports (3 worldwide at the top and near reports after), a profile view with avatar and personal reports, a send emergency alert view with a camera view; a configuration view when the user can put up to 5 contacts to send the alert to them;a send report view with camera and options to configure the camera; a edit report view where the user can see the 3 photos he will update and add a comment of those photos.
Nice to have
• Check the files we are open minds
Should not have
• old design

```html
<!DOCTYPE html>
<html lang="en">
<head>
<meta charset="utf-8">
<title>vigila — app screens</title>
<link href="https://fonts.googleapis.com/css2?family=Roboto:wght@300;400;500&display=swap" rel="stylesheet">
<style>
  :root{
    --bg:#ffffff;
    --red:#c8283f;
    --red-soft:#f25757;
    --maroon:#6b2a30;
    --green:#23836a;
    --ink:#222222;
    --muted:#8a8a8a;
    --bar:#1e1e1e;
    --bar-active:#2b2b2b;
    --cam:#161616;
    --line:#e4e4e4;
  }
  *{box-sizing:border-box;margin:0;padding:0}
  html,body{width:1200px;height:675px;overflow:hidden;background:var(--bg);font-family:"Roboto",sans-serif;color:var(--ink)}
  .canvas{position:relative;width:1200px;height:675px}
  .screen{position:absolute;top:146px;width:208px;height:369px;background:#fff;overflow:hidden;border:1px solid #d9d9d9}
  .screen--splash{left:72px}
  .screen--home{left:358px}
  .screen--report{left:647px}
  .screen--trending{left:939px}

  .status{position:absolute;top:0;left:0;right:0;height:12px;display:flex;justify-content:space-between;align-items:center;padding:0 5px;font-size:6.5px;color:#333;background:#fff;z-index:2;white-space:nowrap}
  .status--clear{background:transparent}
  .status__left{display:flex;align-items:center;gap:3px}
  .status__time{position:absolute;left:50%;transform:translateX(-50%)}

  .header{position:absolute;top:12px;left:0;right:0;height:29px;background:var(--red);color:#fff;font-size:10.5px;font-weight:500;display:flex;align-items:center;justify-content:center}
  .header__search{position:absolute;right:8px;top:8px}

  .tabbar{position:absolute;bottom:0;left:0;right:0;height:33px;background:var(--bar);display:flex}
  .tab{flex:1;display:flex;align-items:center;justify-content:center;position:relative}
  .tab--active{background:var(--bar-active)}
  .tab--active::after{content:"";position:absolute;left:0;right:0;bottom:0;height:2px;background:var(--red)}

  /* splash */
  .splash__backdrop{position:absolute;inset:0;background:linear-gradient(160deg,#f3ece6,#efe6df 50%,#ece9ea)}
  .brand{position:absolute;top:150px;left:0;right:0;display:flex;align-items:center;justify-content:center;gap:7px}
  .brand__square{width:18px;height:18px;background:var(--red)}
  .brand__name{font-size:30px;font-weight:400;color:#333;line-height:1}

  /* home */
  .option{position:absolute;left:0;right:0;color:#fff;padding-left:13px}
  .option--kidnap{top:41px;height:97px;background:var(--red-soft)}
  .option--accuse{top:138px;height:98px;background:var(--maroon)}
  .option--config{top:236px;height:100px;background:var(--green)}
  .option__title{position:absolute;top:39px;font-size:13.5px;font-weight:400;line-height:1;white-space:nowrap}
  .option__sub{position:absolute;top:55px;font-size:5.5px;font-weight:300;white-space:nowrap}
  .option__icon{position:absolute;right:12px;top:40px;width:28px;height:30px;border-radius:3px;background:rgba(255,255,255,.22)}

  /* report */
  .viewfinder{position:absolute;top:41px;left:0;right:0;height:220px;background:linear-gradient(150deg,#c9ccd0,#5d636c 55%,#9aa0a6)}
  .controls{position:absolute;top:261px;left:0;right:0;height:75px;background:var(--cam)}
  .controls__grid{position:absolute;left:12px;top:25px;width:24px;height:24px;border:1.3px solid #ddd;border-radius:50%;display:flex;align-items:center;justify-content:center}
  .controls__shutter{position:absolute;left:50%;top:14px;transform:translateX(-50%);width:46px;height:46px;border:2px solid #eee;border-radius:50%;display:flex;align-items:center;justify-content:center}
  .controls__shutter span{width:38px;height:38px;border-radius:50%;background:#c8c8c8}
  .controls__video{position:absolute;right:14px;top:31px}

  /* trending */
  .segment{position:absolute;top:47px;left:28px;width:148px;height:18px;border:1px solid var(--red);border-radius:9px;display:flex;overflow:hidden;font-size:6px}
  .segment__item{flex:1;display:flex;align-items:center;justify-content:center;color:var(--red)}
  .segment__item--on{background:var(--red);color:#fff}
  .post__head{position:absolute;left:6px;right:6px;display:flex;align-items:center;gap:5px;font-size:7px;color:var(--red);font-weight:500}
  .post__head--first{top:74px}
  .post__head--next{top:310px}
  .post__avatar{width:12px;height:12px;border-radius:50%;background:#c7a58c}
  .post__time{margin-left:auto;color:#555;font-size:5.5px;font-weight:400}
  .post__photo{position:absolute;top:89px;height:193px}
  .post__photo--left{left:0;width:102px;background:linear-gradient(160deg,#8b7266,#5a3f36)}
  .post__photo--right{left:103px;width:105px;background:linear-gradient(170deg,#9fb8d0,#8a7a6c 60%,#d9d4cc)}
  .post__tags{position:absolute;top:288px;left:6px;right:6px;font-size:5px;color:#444;display:flex;align-items:center;white-space:nowrap}
  .post__tags b{color:var(--red);font-weight:500;margin-right:3px}
  .post__more{margin-left:auto;font-size:6px}
  .post__divider{position:absolute;top:302px;left:0;right:0;height:1px;background:var(--line)}
</style>
</head>
<body>
<div class="canvas">

  <!-- Splash -->
  <section class="screen screen--splash">
    <div class="splash__backdrop" role="img" aria-label="Soft collage of smiling community member portraits"></div>
    <div class="status status--clear"><span class="status__left">●●●○○ NOVA</span><span class="status__time">4:21 PM</span><span>22%</span></div>
    <div class="brand"><span class="brand__square"></span><span class="brand__name">vigila</span></div>
  </section>

  <!-- Home -->
  <section class="screen screen--home">
    <div class="status"><span class="status__left">●●●○○ NOVA</span><span class="status__time">4:21 PM</span><span>22%</span></div>
    <header class="header">Home</header>
    <div class="option option--kidnap">
      <p class="option__title">Getting Kidnapped</p>
      <p class="option__sub">Send an alert in case you are getting kidnapped</p>
      <div class="option__icon" role="img" aria-label="Illustration of a kidnapping threat"></div>
    </div>
    <div class="option option--accuse">
      <p class="option__title">Accuse</p>
      <p class="option__sub">accuse someone for something</p>
      <div class="option__icon" role="img" aria-label="Illustration of a masked suspect"></div>
    </div>
    <div class="option option--config">
      <p class="option__title">Configuration</p>
      <p class="option__sub">To set your emergency contact numbers</p>
      <div class="option__icon" role="img" aria-label="Illustration of a person with settings gears"></div>
    </div>
    <nav class="tabbar">
      <div class="tab tab--active"><svg width="11" height="10" viewBox="0 0 11 10"><path d="M5.5 0 11 5H9.5v5H6.5V7h-2v3H1.5V5H0z" fill="#ddd"/></svg></div>
      <div class="tab"><svg width="10" height="10" viewBox="0 0 10 10"><circle cx="5" cy="5" r="5" fill="#bbb"/><path d="M5 2v3h2" stroke="#1e1e1e" stroke-width="1.2" fill="none"/></svg></div>
      <div class="tab"><svg width="12" height="10" viewBox="0 0 12 10"><rect width="12" height="10" rx="2" fill="#c8283f"/><circle cx="6" cy="5" r="2.6" fill="#1e1e1e"/></svg></div>
      <div class="tab"><svg width="11" height="9" viewBox="0 0 11 9"><path d="M0 9h2V7H0zM3 9h2V5H3zM6 9h2V3H6zM9 9h2V0H9z" fill="#bbb"/></svg></div>
      <div class="tab"><svg width="9" height="10" viewBox="0 0 9 10"><circle cx="4.5" cy="3" r="2.6" fill="#bbb"/><path d="M0 10c0-3 2-4.5 4.5-4.5S9 7 9 10z" fill="#bbb"/></svg></div>
    </nav>
  </section>

  <!-- Report -->
  <section class="screen screen--report">
    <div class="status"><span class="status__left">●●●○○ NOVA</span><span class="status__time">4:21 PM</span><span>22%</span></div>
    <header class="header">Report</header>
    <div class="viewfinder" role="img" aria-label="Camera preview of a street confrontation"></div>
    <div class="controls">
      <div class="controls__grid"><svg width="10" height="10" viewBox="0 0 10 10" fill="#ddd"><circle cx="2" cy="2" r="1.2"/><circle cx="5" cy="2" r="1.2"/><circle cx="8" cy="2" r="1.2"/><circle cx="2" cy="5" r="1.2"/><circle cx="5" cy="5" r="1.2"/><circle cx="8" cy="5" r="1.2"/><circle cx="2" cy="8" r="1.2"/><circle cx="5" cy="8" r="1.2"/><circle cx="8" cy="8" r="1.2"/></svg></div>
      <div class="controls__shutter"><span></span></div>
      <svg class="controls__video" width="17" height="10" viewBox="0 0 17 10"><rect width="11" height="10" rx="1" fill="#eee"/><path d="M12 5l5-4v8z" fill="#eee"/></svg>
    </div>
    <nav class="tabbar">
      <div class="tab"><svg width="11" height="10" viewBox="0 0 11 10"><path d="M5.5 0 11 5H9.5v5H6.5V7h-2v3H1.5V5H0z" fill="#bbb"/></svg></div>
      <div class="tab"><svg width="10" height="10" viewBox="0 0 10 10"><circle cx="5" cy="5" r="5" fill="#bbb"/><path d="M5 2v3h2" stroke="#1e1e1e" stroke-width="1.2" fill="none"/></svg></div>
      <div class="tab tab--active"><svg width="12" height="10" viewBox="0 0 12 10"><rect width="12" height="10" rx="2" fill="#c8283f"/><circle cx="6" cy="5" r="2.6" fill="#2b2b2b"/></svg></div>
      <div class="tab"><svg width="11" height="9" viewBox="0 0 11 9"><path d="M0 9h2V7H0zM3 9h2V5H3zM6 9h2V3H6zM9 9h2V0H9z" fill="#bbb"/></svg></div>
      <div class="tab"><svg width="9" height="10" viewBox="0 0 9 10"><circle cx="4.5" cy="3" r="2.6" fill="#bbb"/><path d="M0 10c0-3 2-4.5 4.5-4.5S9 7 9 10z" fill="#bbb"/></svg></div>
    </nav>
  </section>

  <!-- Trending -->
  <section class="screen screen--trending">
    <div class="status"><span class="status__left">●●●○○ NOVA</span><span class="status__time">4:21 PM</span><span>22%</span></div>
    <header class="header">Trending
      <svg class="header__search" width="13" height="13" viewBox="0 0 13 13"><circle cx="5.5" cy="5.5" r="4.5" stroke="#fff" stroke-width="1.2" fill="none"/><path d="M9 9l3.5 3.5" stroke="#fff" stroke-width="1.3"/></svg>
    </header>
    <div class="segment"><span class="segment__item">Most Popular</span><span class="segment__item segment__item--on">Near</span></div>
    <div class="post__head post__head--first"><span class="post__avatar" role="img" aria-label="User avatar"></span>Marco<span class="post__time">10:30</span></div>
    <div class="post__photo post__photo--left" role="img" aria-label="Photo of an injured assault victim"></div>
    <div class="post__photo post__photo--right" role="img" aria-label="Photo of the same person outdoors"></div>
    <div class="post__tags"><b>Marco88</b># Soral # Crime # Orla #<span class="post__more">⋮</span></div>
    <div class="post__divider"></div>
    <div class="post__head post__head--next"><span class="post__avatar" role="img" aria-label="User avatar"></span>Lina<span class="post__time">10:20</span></div>
    <nav class="tabbar">
      <div class="tab"><svg width="11" height="10" viewBox="0 0 11 10"><path d="M5.5 0 11 5H9.5v5H6.5V7h-2v3H1.5V5H0z" fill="#bbb"/></svg></div>
      <div class="tab"><svg width="10" height="10" viewBox="0 0 10 10"><circle cx="5" cy="5" r="5" fill="#888"/><path d="M5 2v3h2" stroke="#1e1e1e" stroke-width="1.2" fill="none"/></svg></div>
      <div class="tab"><svg width="12" height="10" viewBox="0 0 12 10"><rect width="12" height="10" rx="2" fill="#c8283f"/><circle cx="6" cy="5" r="2.6" fill="#1e1e1e"/></svg></div>
      <div class="tab tab--active"><svg width="11" height="9" viewBox="0 0 11 9"><path d="M0 9h2V7H0zM3 9h2V5H3zM6 9h2V3H6zM9 9h2V0H9z" fill="#888"/></svg></div>
      <div class="tab"><svg width="9" height="10" viewBox="0 0 9 10"><circle cx="4.5" cy="3" r="2.6" fill="#888"/><path d="M0 10c0-3 2-4.5 4.5-4.5S9 7 9 10z" fill="#888"/></svg></div>
    </nav>
  </section>

</div>
</body>
</html>
```